Meadowlark Counseling Partners, LLC Needs Modern Business Card Design.

We provide behavioral health services from western Kansas to eastern Kansas. There is an abundance of competition for the services we provide with our main competitor being larger and having significantly more financial resources; however, the quality of services we provide is greater and we have started to catch the attention of the State of Kansas. We had a great logo designed by ArtFolio - this will be used to build upon our brand. The logo (attached) should be used in the card development. We want something unique, modern, but also a card design that clearly states our name, contact info, provides the name and unqiue location of each clinician, etc. Rounded edges, or a unique size, just something that makes our business card stand out from others. I have also uploaded each clinician's name and their unique location and phone number.

Our idea is to have one side be black with our logo. Then, on the other side have business cards for each individual. Plus, we want one card that is "generic" with no specific clinician's name listed so that we can give clients an appointment card when they leave. Some clinicians have two locations - we're open to design and background color, but we have started going with branding colors of black, the yellow in the logo files attached, and sometimes a gray. Our new office has been decorated using this theme.

Target Market(s)

individuals and families in need of behavioral health services; potential professional referral sources; existing referral sources

Industry/Entity Type

Business

Contact Information for Business Card

I attached a Word doc that provides clinician names, credentials and location information specific to each individual.

Font styles to use
Serif

Colors
000000
fbed22
dbdbdb
9d9d9d
c3c3c3

Requirements
Must have
• 1) use of the company logo that has been attached; 2) a template that provides us space to individualize business cards for all of our clinicians; 3) should stick to the colors we are branding with: black, yellow from the logo file, maybe a gray shade and we're open to a suggestion on a shade of white.
Nice to have
• Group discussion culminated in the thought that one side would be black with just our logo - no clinician names, etc. A unique design - rounded edges, unique size, some catchy lay-out would be nice.
Should not have
• Must not be too busy. Should look "clean." The project should stick to branding colors: black, yellow (from the logo file), maybe a gray and shade of white.

```html
<!DOCTYPE html>
<html lang="en">
<head>
<meta charset="utf-8">
<title>Meadowlark Counseling Partners — Business Card</title>
<link rel="stylesheet" href="https://fonts.googleapis.com/css2?family=Exo+2:wght@400;500;600&display=swap">
<style>
  :root {
    --ink: #1f1e1f;
    --gold: #fbd21c;
    --gold-deep: #f9a51f;
    --gold-bright: #fde610;
    --line-gold: #b8950f;
    --paper: #e6e6e6;
    --white: #f2f2f2;
    --dark-text: #1b1b1b;
  }
  * { box-sizing: border-box; margin: 0; padding: 0; }
  html, body {
    width: 1200px; height: 1200px; overflow: hidden;
    background: var(--paper);
    font-family: "Exo 2", sans-serif;
  }
  .canvas {
    width: 1200px; height: 1200px;
    display: flex; flex-direction: column;
    align-items: center; justify-content: center; gap: 44px;
  }
  .card {
    width: 900px; height: 514px;
    border-radius: 44px;
    display: flex; flex-direction: column;
    align-items: center; justify-content: center;
    text-align: center;
  }
  .card--front {
    background: linear-gradient(70deg, var(--gold-deep) 0%, var(--gold) 50%, var(--gold-bright) 100%);
  }
  .card--back { background: var(--ink); }

  .brand {
    display: flex; align-items: center; gap: 18px;
    font-weight: 600; text-transform: uppercase; letter-spacing: 3px;
  }
  .brand__dot { width: 22px; height: 22px; border-radius: 50%; }
  .card--front .brand { color: var(--dark-text); font-size: 34px; }
  .card--front .brand__dot { background: var(--dark-text); }
  .card--back .brand { color: var(--gold); font-size: 24px; margin-bottom: 34px; }
  .card--back .brand__dot { background: var(--gold); width: 16px; height: 16px; }

  .clinician__name {
    color: var(--gold); font-size: 38px; font-weight: 500; letter-spacing: 1px;
  }
  .clinician__role { color: var(--white); font-size: 22px; margin-top: 4px; }
  .divider {
    width: 560px; height: 1px; background: var(--line-gold); margin: 26px 0;
  }
  .contact { color: var(--white); font-size: 24px; line-height: 1.6; }
</style>
</head>
<body>
<main class="canvas">
  <section class="card card--front" aria-label="Card front">
    <div class="brand"><span class="brand__dot"></span>Meadowlark Counseling Partners, LLC</div>
  </section>

  <section class="card card--back" aria-label="Card back">
    <div class="brand"><span class="brand__dot"></span>Meadowlark Counseling Partners, LLC</div>
    <p class="clinician__name">EVERETT J. LOWRY, LP</p>
    <p class="clinician__role">President</p>
    <div class="divider"></div>
    <div class="contact">
      <p>(316) 555-0147</p>
      <p>418 N. Prairie Ave. Wichita, Kansas 67214</p>
    </div>
  </section>
</main>
</body>
</html>
```